New Architectural Firm Business Cards

New Business card to compliment previous pixel forum logo (attached). Please design a business card that is simple, modern, creative....please do not use "symbols", simply the logo and associated graphics/text. The front should contain name/address/phone/email/web address (with graphics).....back should be 100% graphic design using the logo somehow. Hoping for a two color (black and yellow) design. full bleed design, no borders

Target Market(s)

Commercial Architecture Clients

Industry/Entity Type

Architecture

Contact Information for Business Card

Please design a business card that is simple, modern, creative....please do not use "symbols", simply the logo and associated graphics/text. The front should contain name/address/phone/email/web address (with graphics).....back should be 100% graphic design using the logo somehow

Font styles to use
Sans Serif

Colors
FFF300
FFF600
FEFA6F
FFFEC7
FFFEE8

Requirements
Must have
• Clean, Modern Design
Should not have
• Stock images or "icons"

```html
<!DOCTYPE html>
<html lang="en">
<head>
<meta charset="utf-8">
<title>Lumen Architecture – Business Cards</title>
<link rel="stylesheet" href="https://fonts.googleapis.com/css2?family=Poppins:wght@400;500;600;700&display=swap">
<style>
  :root {
    --yellow: #f5c211;
    --black: #0b0b0b;
    --paper: #ffffff;
    --canvas: #ececec;
    --sketch-a: #f7f7f7;
    --sketch-b: #ececec;
    --ghost: #f0f0f0;
  }
  * { margin: 0; padding: 0; box-sizing: border-box; }
  html, body { width: 1200px; height: 2249px; overflow: hidden; }
  body { background: var(--canvas); font-family: "Poppins", sans-serif; color: var(--black); position: relative; }

  .card {
    position: absolute; left: 180px; width: 840px; height: 480px;
    background: var(--paper); overflow: hidden;
    box-shadow: 0 4px 8px rgba(0,0,0,0.22);
  }
  .card--back { top: 1025px; }
  .card--front { top: 1630px; }

  .sketch-area { position: absolute; }
  .card--back .sketch-area {
    left: 0; top: 0; width: 330px; height: 360px;
    background: linear-gradient(135deg, var(--sketch-a), var(--paper) 80%);
  }
  .card--front .sketch-area {
    right: 0; top: 20px; width: 440px; height: 430px;
    background: linear-gradient(200deg, var(--sketch-a), var(--paper) 85%);
  }

  .ghost-name {
    position: absolute; left: 560px; top: 150px;
    font-weight: 700; font-size: 190px; line-height: 1;
    color: var(--ghost); letter-spacing: -4px; white-space: nowrap;
  }

  .brand { position: absolute; color: var(--yellow); font-weight: 700; line-height: 1; text-align: center; }
  .brand__name { display: block; }
  .brand__line { display: block; }
  .card--back .brand { left: 270px; top: 100px; width: 340px; }
  .card--back .brand__name { font-size: 110px; letter-spacing: -3px; }
  .card--back .brand__line { font-size: 40px; margin-top: 38px; }
  .card--front .brand { left: 560px; top: 150px; width: 250px; }
  .card--front .brand__name { font-size: 78px; letter-spacing: -2px; }
  .card--front .brand__line { font-size: 30px; margin-top: 30px; }

  .rule-black { position: absolute; left: 0; width: 100%; height: 9px; background: var(--black); }
  .band-yellow { position: absolute; left: 0; width: 100%; background: var(--yellow); }
  .card--back .rule-black { top: 368px; }
  .card--back .band-yellow { top: 383px; height: 97px; }
  .card--front .rule-black { top: 455px; }
  .card--front .band-yellow { top: 470px; height: 10px; }

  .web-url {
    position: absolute; left: 0; top: 383px; width: 100%; height: 97px;
    display: flex; align-items: center; justify-content: center;
    font-weight: 700; font-size: 27px; letter-spacing: 7px; color: var(--black);
  }
  .web-url__domain { color: var(--paper); }

  .person { position: absolute; left: 45px; top: 52px; }
  .person__name { font-size: 44px; font-weight: 400; line-height: 1; letter-spacing: -0.5px; }
  .person__name strong { color: var(--yellow); font-weight: 600; }
  .person__role { color: var(--yellow); font-weight: 600; font-size: 24px; margin-top: 8px; }

  .contact-list { position: absolute; left: 47px; top: 192px; list-style: none; }
  .contact-list li { display: flex; align-items: center; height: 37px; margin-bottom: 15px; font-size: 20px; }
  .contact-icon { width: 37px; height: 37px; margin-right: 20px; flex: none; }
</style>
</head>
<body>

  <section class="card card--back" aria-label="Card back">
    <div class="sketch-area" role="img" aria-label="Faint line sketch of a commercial building"></div>
    <div class="ghost-name" aria-hidden="true">Lumen</div>
    <div class="brand">
      <span class="brand__name">Lumen</span>
      <span class="brand__line">ARCHITECTURE</span>
    </div>
    <div class="rule-black"></div>
    <div class="band-yellow"></div>
    <p class="web-url">www.&nbsp;<span class="web-url__domain">lumenarch</span>.com</p>
  </section>

  <section class="card card--front" aria-label="Card front">
    <div class="sketch-area" role="img" aria-label="Faint line sketch of a multi-storey office building"></div>
    <div class="person">
      <h1 class="person__name">OWEN <strong>CARTER</strong></h1>
      <p class="person__role">DIRECTOR</p>
    </div>
    <ul class="contact-list">
      <li>
        <svg class="contact-icon" viewBox="0 0 37 37"><rect x="1.5" y="1.5" width="34" height="34" rx="5" fill="#f5c211" stroke="#0b0b0b" stroke-width="3"/><rect x="6" y="6" width="25" height="25" rx="3" fill="#0b0b0b"/><path d="M13 11c1-1 2 0 3 2s0 2.5-1 3c1 2 3 4 5 5 .5-1 1-2 3-1s3 2 2 3c-1 2-3 2.5-6 1s-6-5-7-8 0-4 1-5z" fill="#f5c211"/></svg>
        +100 555 01234
      </li>
      <li>
        <svg class="contact-icon" viewBox="0 0 37 37"><rect x="1.5" y="1.5" width="34" height="34" rx="5" fill="#f5c211" stroke="#0b0b0b" stroke-width="3"/><path d="M18.5 8a6 6 0 0 1 6 6c0 4.5-6 10-6 10s-6-5.5-6-10a6 6 0 0 1 6-6z" fill="#0b0b0b"/><circle cx="18.5" cy="14" r="2.3" fill="#f5c211"/><ellipse cx="18.5" cy="27" rx="8" ry="2.2" fill="none" stroke="#0b0b0b" stroke-width="2"/></svg>
        17/4 Harlow Lane, Canada
      </li>
      <li>
        <svg class="contact-icon" viewBox="0 0 37 37"><rect x="1.5" y="1.5" width="34" height="34" rx="5" fill="#f5c211" stroke="#0b0b0b" stroke-width="3"/><rect x="8" y="11" width="21" height="15" fill="#0b0b0b"/><path d="M8 11l10.5 9L29 11M8 26l7-7M29 26l-7-7" fill="none" stroke="#f5c211" stroke-width="1.5"/></svg>
        hello@lumenstudio.com
      </li>
      <li>
        <svg class="contact-icon" viewBox="0 0 37 37"><rect x="1.5" y="1.5" width="34" height="34" rx="5" fill="#f5c211" stroke="#0b0b0b" stroke-width="3"/><circle cx="18.5" cy="18.5" r="10" fill="#0b0b0b"/><g fill="none" stroke="#f5c211" stroke-width="1.3"><ellipse cx="18.5" cy="18.5" rx="4.5" ry="10"/><path d="M8.5 18.5h20M10 13.5h17M10 23.5h17M18.5 8.5v20"/></g></svg>
        www.lumenarch.com
      </li>
    </ul>
    <div class="brand">
      <span class="brand__name">Lumen</span>
      <span class="brand__line">ARCHITECTURE</span>
    </div>
    <div class="rule-black"></div>
    <div class="band-yellow"></div>
  </section>

</body>
</html>
```